Business Card Design Project

"Crestline Record Services" is database management company working in the direct marketing & digital printing industries. Currently going through a name & rebranding process we require a new company business card.

Industry/Entity Type

Marketing

```html
<!DOCTYPE html>
<html lang="en">
<head>
<meta charset="utf-8">
<title>Crestline Record Services – Business Cards</title>
<link rel="stylesheet" href="https://fonts.googleapis.com/css2?family=Saira:wght@400;500;600;700&display=swap">
<style>
  :root {
    --stage: #e9e7e3;
    --blue: #1686cc;
    --blue-deep: #0f6fb4;
    --blue-light: #2a9be0;
    --paper: #f1f2f4;
    --slate: #4a5260;
    --white: #ffffff;
    --shadow: rgba(20, 30, 45, 0.22);
  }
  * { box-sizing: border-box; margin: 0; padding: 0; }
  html, body { width: 1200px; height: 880px; overflow: hidden; }
  body {
    background: var(--stage);
    font-family: "Saira", "Segoe UI", sans-serif;
    position: relative;
  }
  .card {
    position: absolute;
    width: 540px;
    height: 308px;
    border-radius: 4px;
    overflow: hidden;
    box-shadow: 0 14px 30px var(--shadow);
  }

  /* Front */
  .card--front {
    left: 90px;
    top: 470px;
    background: linear-gradient(160deg, var(--blue-light) 0%, var(--blue) 50%, var(--blue-deep) 100%);
  }
  .card--front .brand {
    position: absolute;
    left: 0; right: 0; top: 104px;
    display: flex;
    justify-content: center;
    align-items: center;
    gap: 14px;
    color: var(--white);
  }
  .card--front .brand-dot {
    width: 34px; height: 34px;
    border-radius: 50%;
    background: var(--white);
    opacity: 0.9;
  }
  .card--front .brand-name {
    font-size: 29px;
    font-weight: 600;
    letter-spacing: 0.5px;
    line-height: 1.1;
  }
  .card--front .front-web {
    position: absolute;
    left: 0; right: 0; bottom: 26px;
    text-align: center;
    color: var(--white);
    font-size: 14px;
    letter-spacing: 3px;
    font-weight: 500;
  }

  /* Back */
  .card--back {
    left: 590px;
    top: 110px;
    background: var(--paper);
  }
  .back-waves { position: absolute; inset: 0; width: 100%; height: 100%; }
  .card--back .brand {
    position: absolute;
    left: 30px; top: 34px;
    display: flex;
    align-items: center;
    gap: 12px;
    color: var(--slate);
  }
  .card--back .brand-dot {
    width: 28px; height: 28px;
    border-radius: 50%;
    background: var(--blue);
  }
  .card--back .brand-name {
    font-size: 23px;
    font-weight: 600;
    letter-spacing: 0.4px;
  }
  .holder {
    position: absolute;
    left: 30px; top: 166px;
    color: var(--white);
  }
  .holder-name { font-size: 21px; font-weight: 700; line-height: 1.15; }
  .holder-role { font-size: 12px; font-weight: 400; opacity: 0.9; }
  .contacts {
    position: absolute;
    right: 24px; top: 178px;
    width: 270px;
    list-style: none;
    color: var(--white);
    font-size: 12px;
    line-height: 1;
  }
  .contacts li {
    display: flex;
    justify-content: flex-end;
    align-items: center;
    gap: 8px;
    height: 17px;
  }
  .contacts .divider {
    height: 1px;
    background: rgba(255, 255, 255, 0.75);
    margin: 5px 0;
  }
  .contacts svg { width: 11px; height: 11px; flex: none; fill: var(--white); }
</style>
</head>
<body>

<section class="card card--front" aria-label="Business card front">
  <div class="brand">
    <span class="brand-dot"></span>
    <span class="brand-name">Crestline Record Services</span>
  </div>
  <p class="front-web">www.crestlinerecords.com</p>
</section>

<section class="card card--back" aria-label="Business card back">
  <svg class="back-waves" viewBox="0 0 540 308" preserveAspectRatio="none" aria-hidden="true">
    <path d="M0 112 C160 116 320 196 540 110 L540 308 L0 308 Z" fill="var(--slate)"/>
    <path d="M0 120 C160 124 320 204 540 120 L540 308 L0 308 Z" fill="var(--white)"/>
    <path d="M0 124 C160 128 320 208 540 126 L540 308 L0 308 Z" fill="var(--blue)"/>
  </svg>

  <div class="brand">
    <span class="brand-dot"></span>
    <span class="brand-name">Crestline Record Services</span>
  </div>

  <div class="holder">
    <p class="holder-name">Name Surname</p>
    <p class="holder-role">manager/CEO</p>
  </div>

  <ul class="contacts">
    <li>+00 123 456 789
      <svg viewBox="0 0 12 12"><rect x="3" y="0.5" width="6" height="11" rx="1"/></svg></li>
    <li>+00 123 456 789
      <svg viewBox="0 0 12 12"><path d="M1 3h10v8H1z M3 0h6v3H3z"/></svg></li>
    <li>name.surname@crestlinerecords.com
      <svg viewBox="0 0 12 12"><path d="M0 2h12v8H0z"/><path d="M0 2l6 4 6-4" fill="none" stroke="#1686cc" stroke-width="1"/></svg></li>
    <li>www.crestlinerecords.com
      <svg viewBox="0 0 12 12"><circle cx="6" cy="6" r="5" fill="none" stroke="#fff" stroke-width="1.2"/><path d="M1 6h10M6 1v10" stroke="#fff" stroke-width="1"/></svg></li>
    <li class="divider"></li>
    <li>Your Address Goes Here</li>
    <li>City, Country, Zipcode
      <svg viewBox="0 0 12 12"><path d="M6 0a4 4 0 0 1 4 4c0 3-4 8-4 8S2 7 2 4a4 4 0 0 1 4-4z"/><circle cx="6" cy="4" r="1.5" fill="#1686cc"/></svg></li>
  </ul>
</section>

</body>
</html>
```